Postcard design

I would like to create a 6x9 Postcard that we can mail to prospective customers marketing commerical printing with a theme around the 4th of July and America's 250th Birthday. Some of the items are below, but we dont need to use all of them, its just as a reference. We are trying to get prospective and existing customer to contact us for their printing.
Business Cards
Brochures
Postcards
Mailing Services (this is a big one)
Flyers
Envelopes
Booklets
Signage
Large Format
Banners
Promo Items
Apparel
Also to note: We are a Faith Based Family owned, 96 year old Commercial Printing Company

```html
<!DOCTYPE html>
<html lang="en">
<head>
<meta charset="utf-8">
<title>Northpine – America's 250th Postcard</title>
<link href="https://fonts.googleapis.com/css2?family=Montserrat:wght@400;500;600;700;800&family=Allura&display=swap" rel="stylesheet">
<style>
:root{
  --navy:#17224a;
  --navy-deep:#0f1838;
  --red:#d3243a;
  --red-dark:#a81a2c;
  --white:#ffffff;
  --paper:#f4f4f6;
  --backdrop:#c4c0bf;
  --line:#dcdce2;
  --sans:'Montserrat', Arial, sans-serif;
  --script:'Allura', cursive;
}
*{box-sizing:border-box;margin:0;padding:0}
html,body{width:1200px;height:2383px;overflow:hidden}
body{background:var(--backdrop);position:relative;font-family:var(--sans);color:var(--navy)}
.card{position:absolute;left:109px;width:982px;height:655px;overflow:hidden;box-shadow:0 2px 10px rgba(0,0,0,.12)}
.front{top:871px;background:var(--navy)}
.back{top:1602px;background:var(--white)}
.abs{position:absolute}

/* front hero */
.hero-scene{position:absolute;left:330px;top:0;width:652px;height:450px;
  background:radial-gradient(ellipse 260px 200px at 300px 330px,#f3a86a 0%,#b0584a 35%,rgba(60,40,80,.6) 65%,transparent 85%),
  radial-gradient(circle 120px at 220px 90px,rgba(214,74,74,.45),transparent 70%),
  radial-gradient(circle 100px at 470px 60px,rgba(230,90,80,.35),transparent 70%),
  var(--navy)}
.stars{left:135px;top:40px;width:140px;height:40px}
.celebrating{left:0;width:406px;top:95px;text-align:center;color:var(--white);font-size:17px;letter-spacing:12px;font-weight:500}
.americas{left:0;width:406px;top:115px;text-align:center;color:var(--white);font-size:41px;font-weight:800}
.big-250{left:45px;top:150px;color:var(--white);font-size:168px;font-weight:800;letter-spacing:-14px;line-height:1}
.big-th{left:368px;top:218px;color:var(--white);font-size:32px;font-weight:500}
.ribbon{left:45px;top:330px;width:315px;height:80px}
.years{left:0;width:406px;top:356px;text-align:center;color:var(--white);font-size:17px;font-weight:700}
.proud{left:640px;width:340px;top:255px;text-align:center}
.proud h2{color:var(--red);font-size:20px;font-weight:800}
.proud .script{font-family:var(--script);color:var(--white);font-size:37px;line-height:.9;margin-top:0}
.proud p{color:var(--white);font-size:11.5px;line-height:1.25;margin-top:6px}
.tear{position:absolute;left:0;width:100%}
.front-paper{left:0;top:445px;width:100%;height:164px;background:var(--paper)}
.merch{left:645px;top:380px;width:325px;height:218px;border-radius:4px;
  background:linear-gradient(135deg,#ffffff 0%,#e6e8ef 40%,#c9cfdd 70%,#b84050 100%);opacity:.95}
.logo{display:flex;align-items:center;gap:8px}
.logo .name{font-weight:600;color:var(--navy);letter-spacing:1px}
.logo .mark{background:var(--red)}
.front-logo{left:50px;top:472px}
.front-logo .name{font-size:40px}
.front-logo .mark{width:22px;height:22px}
.tagline{color:var(--navy);font-weight:600;letter-spacing:4.5px;font-size:10.5px}
.front-tagline{left:63px;top:519px}
.faith{left:52px;top:537px;width:300px;height:22px;background:var(--navy);color:var(--white);
  font-size:11px;letter-spacing:3px;font-weight:600;display:flex;align-items:center;justify-content:center;
  clip-path:polygon(0 0,100% 0,96% 50%,100% 100%,0 100%,4% 50%)}
.maine{left:52px;top:560px;width:300px;text-align:center;font-family:var(--script);color:var(--red);font-size:34px}
.contact-head{left:401px;top:475px;font-size:13px;font-weight:700;color:var(--navy);line-height:1.3}
.contact-list{list-style:none}
.contact-list li{display:flex;align-items:center;gap:16px;font-weight:500;color:var(--navy-deep)}
.front-contacts{left:401px;top:520px}
.front-contacts li{font-size:14.5px;height:27px}
.ico{flex:none;border-radius:50%;display:flex;align-items:center;justify-content:center}
.ico-line{width:20px;height:20px;border:1.5px solid var(--red)}
.ico-line svg{stroke:var(--red)}
.band{left:0;top:609px;width:100%;height:46px;background:var(--red);color:var(--white);display:flex;align-items:center;padding:0 28px;gap:14px;font-size:12.5px;font-weight:600}
.band .bless{font-family:var(--script);font-size:30px;font-weight:400}
.band .sep{width:1px;height:24px;background:rgba(255,255,255,.7);margin:0 8px}

/* back */
.back-panel{left:0;top:0;width:591px;height:655px;background:var(--navy-deep)}
.back-paper{left:0;top:515px;width:591px;height:140px;background:var(--paper)}
.back-head{left:42px;top:34px;font-size:21px;font-weight:700;line-height:1.5}
.back-head .w{color:var(--white)} .back-head .r{color:var(--red)}
.services{left:44px;top:113px;width:520px;display:grid;grid-template-columns:297px 1fr;list-style:none;row-gap:25px}
.services li{display:flex;align-items:center;gap:20px;color:var(--white);font-size:19px;font-weight:500;height:40px}
.ico-fill{width:40px;height:40px;background:var(--red)}
.ico-fill svg{stroke:var(--white)}
.divider{left:293px;top:118px;height:350px;border-left:1px dashed rgba(255,255,255,.3)}
.back-cta{left:54px;top:555px;font-weight:700;font-size:19px;line-height:1.15;color:var(--navy)}
.back-cta .r{color:var(--red);font-size:17px}
.back-contacts{left:330px;top:548px}
.back-contacts li{font-size:15px;height:33px;gap:18px}
.ico-navy{width:28px;height:28px;background:var(--navy)}
.ico-navy svg{stroke:var(--white)}
.back-logo{left:623px;top:44px}
.back-logo .name{font-size:29px}
.back-logo .mark{width:16px;height:16px}
.back-tagline{left:634px;top:79px;font-size:8px;letter-spacing:3.5px}
.address{left:623px;top:100px;font-size:14px;font-weight:500;line-height:1.35;color:var(--navy)}
.stamp{left:880px;top:33px;width:76px;height:76px;background:#f1f1f3}
.addr-line{left:640px;width:295px;border-top:1px solid var(--line)}
</style>
</head>
<body>

<!-- FRONT -->
<section class="card front" aria-label="Postcard front">
  <div class="hero-scene" role="img" aria-label="Fireworks over an American flag on a pole beside a cross, with a family silhouette standing on a hill at sunset"></div>

  <svg class="abs stars" viewBox="0 0 140 40" aria-hidden="true">
    <g fill="#d3243a">
      <polygon points="10,30 12,35 17,35 13,38 15,43 10,40 5,43 7,38 3,35 8,35" transform="translate(0,-8)"/>
      <polygon points="38,20 40.5,26 47,26 42,30 44,36 38,32 32,36 34,30 29,26 35.5,26" transform="translate(0,-4)"/>
      <polygon points="102,20 104.5,26 111,26 106,30 108,36 102,32 96,36 98,30 93,26 99.5,26" transform="translate(0,-4)"/>
      <polygon points="130,30 132,35 137,35 133,38 135,43 130,40 125,43 127,38 123,35 128,35" transform="translate(0,-8)"/>
    </g>
    <polygon fill="#fff" points="70,0 74,11 86,11 76,18 80,30 70,23 60,30 64,18 54,11 66,11"/>
  </svg>
  <div class="abs celebrating">CELBRATING</div>
  <div class="abs americas">AMERICA’S</div>
  <div class="abs big-250">250</div>
  <div class="abs big-th">th</div>

  <svg class="abs ribbon" viewBox="0 0 315 80" aria-hidden="true">
    <polygon points="0,30 30,24 30,62 8,66 18,48" fill="#a81a2c"/>
    <polygon points="315,30 285,24 285,62 307,66 297,48" fill="#a81a2c"/>
    <path d="M18,18 Q157,-6 297,18 L297,48 Q157,26 18,48 Z" fill="#d3243a"/>
  </svg>
  <div class="abs" style="left:68px;top:335px;width:270px;text-align:center;color:#fff;font-size:17px;font-weight:700;transform:rotate(-2deg)">250 YEARS OF FREEDOM</div>
  <div class="abs years" style="top:380px">1776-2026</div>

  <div class="abs proud">
    <h2>PROUD TO STAND</h2>
    <div class="script">For a Stronger Tomorrow</div>
    <p>For 94 years The Northpine Group has been serving the people and businesses of Maine with High Quality Printing and Mailing services you can count on.</p>
  </div>

  <svg class="tear" style="top:430px;height:22px" viewBox="0 0 982 22" preserveAspectRatio="none" aria-hidden="true">
    <polygon fill="#f4f4f6" points="0,14 30,10 55,16 90,8 130,13 170,6 200,12 240,9 280,4 310,12 350,7 390,13 430,8 470,11 510,5 550,12 590,9 630,14 670,7 710,12 750,9 790,13 830,6 870,11 910,8 950,13 982,9 982,22 0,22"/>
  </svg>
  <div class="abs front-paper"></div>
  <div class="abs merch" role="img" aria-label="Branded merchandise: polo shirt, tote bag, brochures, booklets, mug, water bottle, business cards and envelopes"></div>

  <div class="abs logo front-logo"><span class="name">NORTHPINE</span><span class="mark"></span></div>
  <div class="abs tagline front-tagline">PRINTING | MAILING | SIGNAGE</div>
  <div class="abs faith">FAITH BASED.FAMILY OWEND</div>
  <div class="abs maine">Maine Made!</div>

  <div class="abs contact-head">CONTACT US TODAY FOR ALL<br>YOUR PRINTING NEEDS!</div>
  <ul class="abs contact-list front-contacts">
    <li><span class="ico ico-line"><svg width="11" height="11" viewBox="0 0 24 24" fill="none" stroke-width="2.5"><path d="M5 3h4l2 5-3 2a12 12 0 0 0 6 6l2-3 5 2v4a2 2 0 0 1-2 2A17 17 0 0 1 3 5a2 2 0 0 1 2-2z"/></svg></span>(555) 014-2200</li>
    <li><span class="ico ico-line"><svg width="11" height="11" viewBox="0 0 24 24" fill="none" stroke-width="2.5"><rect x="3" y="5" width="18" height="14"/><path d="M3 6l9 7 9-7"/></svg></span>hello@northpineprint.com</li>
    <li><span class="ico ico-line"><svg width="11" height="11" viewBox="0 0 24 24" fill="none" stroke-width="2.5"><circle cx="12" cy="12" r="9"/><path d="M3 12h18M12 3c3 3 3 15 0 18M12 3c-3 3-3 15 0 18"/></svg></span><span>www.<b style="font-weight:600">northpineprint</b>.com</span></li>
  </ul>

  <div class="abs band">
    <span>★ ★</span>
    <span>THANK YOU FOR SUPPORTING LOCAL, FAITH-BASED, FAMILY OWNED BUSINESSES.</span>
    <span class="sep"></span>
    <span class="bless">God Bless America</span>
    <span>★ ★</span>
  </div>
</section>

<!-- BACK -->
<section class="card back" aria-label="Postcard back">
  <div class="abs back-panel"></div>
  <div class="abs back-head"><div class="w">LET US HELP YOU SHARE YOUR MESSAGE.</div><div class="r">PRINTING SOLUTIONS THAT MAKE AN IMPACT.</div></div>
  <div class="abs divider"></div>
  <ul class="abs services">
    <li><span class="ico ico-fill"><svg width="20" height="20" viewBox="0 0 24 24" fill="none" stroke-width="1.6"><rect x="3" y="5" width="18" height="14" rx="1"/><circle cx="8" cy="11" r="2"/><path d="M5 16c1-2 5-2 6 0M13 10h5M13 13h5"/></svg></span>Business Cards</li>
    <li><span class="ico ico-fill"><svg width="20" height="20" viewBox="0 0 24 24" fill="none" stroke-width="1.6"><rect x="3" y="6" width="15" height="12" rx="1"/><path d="M7 10h7M7 13h5M18 9l3 1v8l-3 1"/></svg></span>Large Format</li>
    <li><span class="ico ico-fill"><svg width="20" height="20" viewBox="0 0 24 24" fill="none" stroke-width="1.6"><path d="M3 10l9-6 9 6v10H3z"/><path d="M3 10l9 6 9-6"/></svg></span>Mailing Services</li>
    <li><span class="ico ico-fill"><svg width="20" height="20" viewBox="0 0 24 24" fill="none" stroke-width="1.6"><path d="M5 5h11v14H5z"/><path d="M16 8h2a2 2 0 0 1 0 8h-2"/></svg></span>Promo Items</li>
    <li><span class="ico ico-fill"><svg width="20" height="20" viewBox="0 0 24 24" fill="none" stroke-width="1.6"><path d="M3 5l6 2 6-2 6 2v13l-6-2-6 2-6-2z"/><path d="M9 7v13M15 5v13"/></svg></span>Brochures</li>
    <li><span class="ico ico-fill"><svg width="20" height="20" viewBox="0 0 24 24" fill="none" stroke-width="1.6"><rect x="3" y="5" width="18" height="14" rx="1"/><path d="M3 6l9 7 9-7"/></svg></span>Envelopes</li>
    <li><span class="ico ico-fill"><svg width="20" height="20" viewBox="0 0 24 24" fill="none" stroke-width="1.6"><path d="M3 6h8v13H3zM13 6h8v13h-8z"/><path d="M5 9h4M5 12h4M15 9h4M15 12h4"/></svg></span>Booklets</li>
    <li><span class="ico ico-fill"><svg width="20" height="20" viewBox="0 0 24 24" fill="none" stroke-width="1.6"><path d="M8 4l-5 3 2 4 2-1v10h10V10l2 1 2-4-5-3a3 3 0 0 1-8 0z"/></svg></span>Apparel</li>
    <li><span class="ico ico-fill"><svg width="20" height="20" viewBox="0 0 24 24" fill="none" stroke-width="1.6"><path d="M3 4h18M5 4v16M5 8h14v10H5"/></svg></span>Signage</li>
    <li><span class="ico ico-fill"><svg width="20" height="20" viewBox="0 0 24 24" fill="none" stroke-width="1.6"><path d="M3 4h18M5 4v11h14V4M8 15v5M16 15v5"/></svg></span>Banners</li>
    <li><span class="ico ico-fill"><svg width="20" height="20" viewBox="0 0 24 24" fill="none" stroke-width="1.6"><rect x="5" y="3" width="14" height="18" rx="1"/><path d="M8 7h8v5H8zM8 15h8M8 18h5"/></svg></span>Flyers</li>
    <li><span class="ico ico-fill"><svg width="20" height="20" viewBox="0 0 24 24" fill="none" stroke-width="1.6"><rect x="3" y="6" width="18" height="12" rx="1"/><path d="M6 9h5v4H6zM14 9h4M14 12h4M14 15h4"/></svg></span>Postcards</li>
  </ul>

  <svg class="tear" style="top:500px;height:22px;width:591px" viewBox="0 0 591 22" preserveAspectRatio="none" aria-hidden="true">
    <polygon fill="#f4f4f6" points="0,14 25,8 50,14 80,6 110,12 140,9 170,14 200,5 230,12 260,8 290,13 320,7 350,12 380,9 410,14 440,6 470,12 500,9 530,13 560,7 591,12 591,22 0,22"/>
  </svg>
  <div class="abs back-paper"></div>
  <div class="abs back-cta"><div class="r">CONTACT US TODAY</div>FOR ALL YOUR<br>PRINTING NEEDS!</div>
  <ul class="abs contact-list back-contacts">
    <li><span class="ico ico-navy"><svg width="14" height="14" viewBox="0 0 24 24" fill="none" stroke-width="2"><path d="M5 3h4l2 5-3 2a12 12 0 0 0 6 6l2-3 5 2v4a2 2 0 0 1-2 2A17 17 0 0 1 3 5a2 2 0 0 1 2-2z"/></svg></span>(555) 014-2200</li>
    <li><span class="ico ico-navy"><svg width="14" height="14" viewBox="0 0 24 24" fill="none" stroke-width="2"><rect x="3" y="5" width="18" height="14"/><path d="M3 6l9 7 9-7"/></svg></span>hello@northpineprint.com</li>
    <li><span class="ico ico-navy"><svg width="14" height="14" viewBox="0 0 24 24" fill="none" stroke-width="2"><circle cx="12" cy="12" r="9"/><path d="M3 12h18M12 3c3 3 3 15 0 18M12 3c-3 3-3 15 0 18"/></svg></span><span>www.<b style="font-weight:600">northpineprint</b>.com</span></li>
  </ul>

  <div class="abs logo back-logo"><span class="name">NORTHPINE</span><span class="mark"></span></div>
  <div class="abs tagline back-tagline">PRINTING | MAILING | SIGNAGE</div>
  <div class="abs address">48 Harbor Mill Road<br>Millbrook, ME 04000</div>
  <div class="abs stamp"></div>
  <div class="abs addr-line" style="top:200px"></div>
  <div class="abs addr-line" style="top:245px"></div>
  <div class="abs addr-line" style="top:290px"></div>
  <div class="abs addr-line" style="top:335px"></div>
  <div class="abs addr-line" style="top:380px"></div>
</section>

</body>
</html>
```